Quotecraft services

I provide collision estimating for autobody shops, so when they need a collision estimate and they are too busy or don't have the software, i write that estimate for them. I do this either in person or virtual. I need a postcard mailer design, 6.25 x 9 inches, with a header that reads QUOTECRAFT SERVICES, highlighting 20+ years of experience, and text that reads ASK ABOUT OUR TRAINING

Target Market(s)

Autobody Repair shops

Industry/Entity Type

Autobody

```html
<!DOCTYPE html>
<html lang="en">
<head>
<meta charset="utf-8">
<title>Quotecraft Services – Postcard</title>
<link href="https://fonts.googleapis.com/css2?family=Bebas+Neue&family=Urbanist:wght@400;500;700;800&display=swap" rel="stylesheet">
<style>
  :root {
    --ink: #000000;
    --night: #141414;
    --smoke: #2a2a2a;
    --flame: #ff3a05;
    --white: #ffffff;
    --photo-warm: #a99a72;
    --photo-cool: #5b5f66;
  }
  * { margin: 0; padding: 0; box-sizing: border-box; }
  html, body { width: 811px; height: 1200px; overflow: hidden; background: var(--ink); }
  .postcard {
    position: relative;
    width: 811px;
    height: 1200px;
    overflow: hidden;
    font-family: "Urbanist", sans-serif;
    color: var(--white);
  }
  .backdrop {
    position: absolute; inset: 0;
    background: radial-gradient(ellipse at 20% 20%, var(--smoke), var(--night) 55%, var(--ink) 100%);
  }
  .hero-photo {
    position: absolute;
    left: 52px; top: 155px;
    width: 710px; height: 480px;
    border-radius: 26px 26px 0 0;
    background: linear-gradient(100deg, var(--photo-warm) 0%, #8d8468 35%, var(--photo-cool) 60%, #2b2b2d 85%, #5a1a22 100%);
  }
  .panel-band {
    position: absolute; left: 0; top: 524px;
    width: 811px; height: 330px;
  }
  .brand {
    position: absolute;
    top: 68px; left: 0; width: 811px;
    display: flex; justify-content: center; align-items: center; gap: 14px;
  }
  .brand-mark { width: 26px; height: 26px; background: var(--flame); }
  .brand-name {
    font-family: "Bebas Neue", sans-serif;
    font-size: 52px; line-height: 1;
    letter-spacing: 3px;
    color: var(--white);
  }
  .headline {
    position: absolute;
    left: 108px; top: 560px;
    font-family: "Bebas Neue", sans-serif;
    font-weight: 400;
    font-size: 150px;
    line-height: 111px;
    letter-spacing: 1px;
    color: var(--white);
  }
  .intro {
    position: absolute;
    left: 111px; top: 798px;
    width: 600px;
    font-size: 25px; line-height: 32px;
    font-weight: 500;
  }
  .intro strong { color: var(--flame); font-weight: 800; }
  .experience { position: absolute; left: 107px; top: 950px; }
  .experience-label {
    font-size: 18px; letter-spacing: 3px; font-weight: 500;
    padding-top: 6px; border-top: 1px solid #555; width: 128px;
    padding-left: 4px;
  }
  .experience-figure {
    font-size: 96px; font-weight: 700; line-height: 72px;
    color: var(--flame); letter-spacing: -2px; margin-top: 6px;
  }
  .experience-caption {
    font-family: "Bebas Neue", sans-serif;
    font-size: 28px; letter-spacing: 3.2px; margin-top: 8px;
  }
  .training-note {
    position: absolute; left: 428px; top: 946px;
    display: flex; align-items: center; gap: 10px;
    font-size: 19px; letter-spacing: 1.6px; font-weight: 500;
  }
  .contact {
    position: absolute; left: 396px; top: 985px;
    width: 358px; height: 104px;
  }
  .contact svg { position: absolute; inset: 0; }
  .contact-text {
    position: relative; text-align: center; padding-left: 20px;
  }
  .contact-phone { font-size: 32px; font-weight: 800; padding-top: 16px; line-height: 40px; letter-spacing: 0.5px; }
  .contact-web { font-size: 19px; font-weight: 500; letter-spacing: 0.6px; }
</style>
</head>
<body>
<main class="postcard">
  <div class="backdrop" role="img" aria-label="Dark, blurred photo of a damaged car and pavement"></div>

  <div class="hero-photo" role="img" aria-label="Photo of an estimator with a clipboard inspecting a damaged rear bumper and tail light"></div>

  <svg class="panel-band" viewBox="0 0 811 330" aria-hidden="true">
    <path fill="var(--ink)" d="M0 0 H200 a25 25 0 0 1 25 25 v58 a25 25 0 0 0 25 25 H558 V25 a25 25 0 0 1 25 -25 H811 V330 H0 Z"/>
  </svg>

  <header class="brand">
    <span class="brand-mark"></span>
    <span class="brand-name">QUOTECRAFT</span>
  </header>

  <h1 class="headline">QUOTECRAFT<br>SERVICES</h1>

  <p class="intro">We provide <strong>accurate collision estimates,</strong> for autobody shops in person or virtually.</p>

  <section class="experience">
    <p class="experience-label">WE HAVE;</p>
    <p class="experience-figure">20+</p>
    <p class="experience-caption">YEARS OF EXPERIENCE</p>
  </section>

  <p class="training-note">
    <svg width="18" height="18" viewBox="0 0 18 18" aria-hidden="true">
      <circle cx="9" cy="9" r="9" fill="var(--flame)"/>
      <path d="M6.3 7a2.7 2.7 0 1 1 3.7 2.5c-.7.3-1 .7-1 1.4v.6" stroke="var(--ink)" stroke-width="2" fill="none" stroke-linecap="round"/>
      <circle cx="9" cy="14" r="1.2" fill="var(--ink)"/>
    </svg>
    ASK ABOUT OUR TRAINING
  </p>

  <div class="contact">
    <svg viewBox="0 0 358 104" aria-hidden="true">
      <path fill="var(--flame)" d="M10 0 H350 a8 8 0 0 1 7 11 L344 52 L357 93 a8 8 0 0 1 -7 11 H10 a8 8 0 0 1 -9 -9 L12 52 L1 9 a8 8 0 0 1 9 -9 Z"/>
    </svg>
    <div class="contact-text">
      <p class="contact-phone">(555) 014-2290</p>
      <p class="contact-web">www.quotecraftservices.com</p>
    </div>
  </div>
</main>
</body>
</html>
```